Business Card Design Project

I am community manager and social media strategist. I need a double sided business card with company logo and name. Looking for something professional, elegant but also a little bit original.

• - The logo and the colours are the company colours and a required to stay.
- The size should be: 84 x 55 mm (or 3.30 x 2.16)
- The file size should be: 1039 x 697 pixels (300 dpi)
- I'd like rounded corners. :)

Use the following contact information for the card:

Léonie Vardin
Stratégie médias sociaux / community management / édition de sites sociaux
mob. : 0687529103
leonie.vardin@postelune.fr
Micro. : @lvardin
Visio : vardin.leonie

```html
<!DOCTYPE html>
<html lang="fr">
<head>
<meta charset="utf-8">
<title>NORVELA — cartes de visite</title>
<link href="https://fonts.googleapis.com/css2?family=Open+Sans:wght@400;700&family=Cutive+Mono&family=Delius&family=Kurale&display=swap" rel="stylesheet">
<style>
  :root{
    --page:#ffffff;
    --frame:#3a3a3a;
    --brand:#17609a;
    --brand-light:#2b8fd0;
    --card:#e6efdb;
    --card-edge:#c9d0c2;
    --band:#b7e0da;
    --band-deep:#9fd3cc;
    --ink:#5a5a5a;
    --name:#4d4d4d;
  }
  *{box-sizing:border-box;margin:0;padding:0}
  html,body{width:1188px;height:1200px;overflow:hidden;background:var(--page)}
  .sheet{position:relative;width:1188px;height:1200px;border:2px solid var(--frame);font-family:"Open Sans",Arial,sans-serif}

  .brand{position:absolute;display:flex;flex-direction:column;align-items:center}
  .brand-dot{border-radius:50%;background:linear-gradient(160deg,var(--brand-light),var(--brand))}
  .brand-name{font-weight:700;color:var(--brand);line-height:1;letter-spacing:.02em}

  .brand--hero{left:44px;top:150px;width:420px}
  .brand--hero .brand-dot{width:232px;height:232px}
  .brand--hero .brand-name{font-size:92px;margin-top:12px}

  .card{position:absolute;background:var(--card);border:2px solid var(--card-edge);border-radius:18px;overflow:hidden}
  .band{position:absolute;background:linear-gradient(180deg,var(--band),var(--band-deep) 50%,var(--band))}
  .band--side{left:0;top:0;bottom:0;width:58px;background:linear-gradient(90deg,var(--band),var(--band-deep) 50%,var(--band))}
  .band--full{left:0;right:0;height:38px}

  .holder{position:absolute;color:var(--name);white-space:nowrap}
  .details{position:absolute;color:var(--ink);font-family:Arial,"Open Sans",sans-serif}
  .details p{margin:0}

  .watermark{position:absolute;left:50%;top:50%;transform:translate(-50%,-50%);opacity:.07}
  .watermark .brand-dot{width:150px;height:150px}
  .watermark .brand-name{font-size:56px;margin-top:6px}

  /* recto, side band */
  .card--recto-side{left:673px;top:172px;width:483px;height:319px}
  .card--recto-side .brand{left:58px;right:0;top:30px}
  .card--recto-side .brand-dot{width:206px;height:184px;border-radius:50%}
  .card--recto-side .brand-name{font-size:64px;margin-top:18px}

  /* verso, mono name */
  .card--verso-mono{left:160px;top:505px;width:483px;height:319px}
  .card--verso-mono .holder{left:0;right:0;top:34px;text-align:center;font-family:"Cutive Mono",monospace;font-size:34px}
  .card--verso-mono .band{top:136px}
  .card--verso-mono .details{left:18px;top:180px;width:440px;font-size:16px;line-height:21px}

  /* verso, script name */
  .card--verso-script{left:685px;top:505px;width:479px;height:319px}
  .card--verso-script .holder{left:14px;top:14px;font-family:"Delius",cursive;font-size:34px}
  .card--verso-script .brand--corner{right:10px;top:8px}
  .card--verso-script .brand--corner .brand-dot{width:66px;height:58px}
  .card--verso-script .brand--corner .brand-name{font-size:26px;margin-top:4px}
  .card--verso-script .details{left:8px;top:112px;width:380px;font-size:12px;line-height:19px}
  .card--verso-script .band{top:244px;height:36px}

  /* recto, bottom band */
  .card--recto-band{left:176px;top:849px;width:479px;height:313px}
  .card--recto-band .brand{left:0;right:0;top:14px}
  .card--recto-band .brand-dot{width:156px;height:146px}
  .card--recto-band .brand-name{font-size:58px;margin-top:12px}
  .card--recto-band .band{top:236px;height:36px}

  /* verso, serif name */
  .card--verso-serif{left:685px;top:839px;width:481px;height:317px}
  .card--verso-serif .holder{left:14px;top:18px;font-family:"Kurale",serif;font-size:38px}
  .card--verso-serif .brand--corner{right:10px;top:12px}
  .card--verso-serif .brand--corner .brand-dot{width:44px;height:38px}
  .card--verso-serif .brand--corner .brand-name{font-size:17px;margin-top:3px}
  .card--verso-serif .band{top:80px;height:36px}
  .card--verso-serif .details{left:14px;top:178px;width:440px;font-size:16px;line-height:20px}
</style>
</head>
<body>
<main class="sheet">

  <div class="brand brand--hero">
    <span class="brand-dot"></span>
    <span class="brand-name">NORVELA</span>
  </div>

  <section class="card card--recto-side">
    <div class="band band--side" role="img" aria-label="Frise décorative de vagues turquoise"></div>
    <div class="brand">
      <span class="brand-dot"></span>
      <span class="brand-name">NORVELA</span>
    </div>
  </section>

  <section class="card card--verso-mono">
    <h2 class="holder">Léonie Vardin</h2>
    <div class="band band--full" role="img" aria-label="Frise décorative de vagues turquoise"></div>
    <div class="details">
      <p>Stratégie médias sociaux / community management / édition de sites sociaux</p>
      <p>mob. : 0687529103</p>
      <p>leonie.vardin@postelune.fr</p>
      <p>Micro. : @lvardin</p>
      <p>Visio : vardin.leonie</p>
    </div>
  </section>

  <section class="card card--verso-script">
    <div class="brand watermark"><span class="brand-dot"></span><span class="brand-name">NORVELA</span></div>
    <h2 class="holder">Léonie Vardin</h2>
    <div class="brand brand--corner">
      <span class="brand-dot"></span>
      <span class="brand-name">NORVELA</span>
    </div>
    <div class="details">
      <p>Stratégie médias sociaux / community management / édition de sites sociaux</p>
      <p>mob. : 0687529103</p>
      <p>leonie.vardin@postelune.fr</p>
      <p>Micro. : @lvardin</p>
      <p>Visio : vardin.leonie</p>
    </div>
    <div class="band band--full" role="img" aria-label="Frise décorative de vagues turquoise"></div>
  </section>

  <section class="card card--recto-band">
    <div class="brand">
      <span class="brand-dot"></span>
      <span class="brand-name">NORVELA</span>
    </div>
    <div class="band band--full" role="img" aria-label="Frise décorative de vagues turquoise"></div>
  </section>

  <section class="card card--verso-serif">
    <div class="brand watermark"><span class="brand-dot"></span><span class="brand-name">NORVELA</span></div>
    <h2 class="holder">Léonie Vardin</h2>
    <div class="brand brand--corner">
      <span class="brand-dot"></span>
      <span class="brand-name">NORVELA</span>
    </div>
    <div class="band band--full" role="img" aria-label="Frise décorative de vagues turquoise"></div>
    <div class="details">
      <p>Stratégie médias sociaux / community management / édition de sites sociaux</p>
      <p>mob. : 0687529103</p>
      <p>leonie.vardin@postelune.fr</p>
      <p>Micro. : @lvardin</p>
      <p>Visio : vardin.leonie</p>
    </div>
  </section>

</main>
</body>
</html>
```